B2B Consulting firm needs a re-fresh of its process diagrams

We are a commercial real estate consulting firm. Think: I wonder who Korvanta uses when they have to build a new plant and sell the old one? That's us! We have created diagrams that we use to demonstrate to our clients the process of the project that they are about to go through. That is our "frontstage" diagram. We also have a "backstage" diagram that we use to train employees and to ensure that we do not make a stupid mistake! Here is a video showing you a little about what we are wanting https://view.clipmarrow.com/v/QpLRZW7BYEK4t8HJ2MVS

Target Market(s)

B2B - C-suite and business leaders

Industry/Entity Type

Commercial Real Estate

Font styles to use
Sans Serif

Colors
0094D4
00A9DD
6FCCEA
C7EBF8
E9F6FB
EB3D1F
EC4F4E
F09395
F8D3D4
FCEDEE

Requirements
Must have
• Think of it as a infographic - clean and modern
Nice to have
• I would suggest that you look at the infographics that are used by Pellingham Trade Journal, Drummoth, TVRL and other professional services firms/publications.

```html
<!DOCTYPE html>
<html lang="en">
<head>
<meta charset="utf-8">
<title>Space Acquisition: Purchase &amp; Process Deliverables</title>
<link href="https://fonts.googleapis.com/css2?family=Arimo:ital,wght@0,400;0,700;1,400;1,700&display=swap" rel="stylesheet">
<style>
  :root{
    --page:#d9d9d9;
    --ink:#061826;
    --ink-soft:#0c2133;
    --band:#2b4d68;
    --rule:#2f5272;
    --white:#ffffff;
    --muted:#b8c2cc;
    --sky:#6fc4ec;
    --navy:#0e4a78;
    --red:#d3302b;
    --light-blue:#6fbfe8;
    --orange:#f3921f;
    --ring:#e4e7eb;
    --connector:#9aa1a8;
  }
  *{box-sizing:border-box;margin:0;padding:0}
  html,body{width:1200px;height:1200px;overflow:hidden}
  body{background:var(--page);font-family:"Arimo",Arial,sans-serif;color:var(--white);position:relative}

  .sheet{position:absolute;left:182px;width:836px;height:470px;background:var(--ink)}
  .sheet--top{top:101px}
  .sheet--bottom{top:636px}

  .timeline{position:absolute;left:0;top:0;width:120px;height:470px;background:var(--white)}
  .timeline svg{position:absolute;left:0;top:0}
  .timeline__label{position:absolute;width:120px;text-align:center;color:#1b2a38}

  .col-process{position:absolute;left:494px;width:141px;bottom:0;background:var(--ink-soft)}
  .band{position:absolute;left:120px;right:0;height:20px;background:var(--band);font-size:8.5px;color:#e8eef3}
  .band span{position:absolute;top:5px;text-align:center}
  .rule{position:absolute;left:120px;right:0;height:1px;background:var(--rule)}

  .t{position:absolute;font-size:7.6px;line-height:10.5px;white-space:nowrap}
  .t b{font-weight:700}
  .center{text-align:center}
  .proc{font-weight:700;font-size:8.6px;line-height:12px}
  .head{font-weight:700;font-size:8.8px}
  .figure{font-style:italic;font-size:10px;color:#a9c7dc}
  ul.dots{list-style:none}
  ul.dots li{position:relative;padding-left:6px}
  ul.dots li::before{content:"";position:absolute;left:0;top:4.5px;width:2px;height:2px;background:var(--white)}
  ul.sq li{padding-left:12px}
  ul.sq li::before{left:2px;width:2.5px;height:2.5px}
  .num{font-weight:700}
  .sub{padding-left:18px;font-style:italic}
  .sub::before{content:"▪ ";font-style:normal;font-size:5px;vertical-align:1px}
  .link-note{color:var(--sky);font-weight:700;font-style:italic;font-size:7.6px;line-height:12px}

  .brand{position:absolute;right:18px;top:32px;display:flex;align-items:center;gap:6px;color:var(--white);font-weight:700;font-size:13px;line-height:14px;white-space:nowrap}
  .brand__mark{width:9px;height:9px;background:var(--white)}
</style>
</head>
<body>

<!-- Sheet one -->
<section class="sheet sheet--top" aria-label="Space acquisition steps 1 to 3">
  <div class="col-process" style="top:100px"></div>

  <div class="timeline">
    <svg width="120" height="470" viewBox="0 0 120 470">
      <circle cx="60" cy="63" r="37" fill="#c7e6f6"/>
      <line x1="60" y1="100" x2="60" y2="280" stroke="var(--connector)" stroke-width="0.8"/>
      <line x1="60" y1="382" x2="60" y2="360" stroke="var(--connector)" stroke-width="0.8"/>
      <path d="M57.5 179 L60 183 L62.5 179Z M57.5 303 L60 307 L62.5 303Z M57.5 376 L60 380 L62.5 376Z" fill="var(--connector)"/>
      <path d="M118 305 H17 V362 M118 377 H17 V433" fill="none" stroke="#7d858c" stroke-width="0.6"/>
      <g transform="translate(60 209)">
        <circle r="25" fill="#fff" stroke="var(--ring)" stroke-width="4"/>
        <circle r="25" fill="none" stroke="var(--navy)" stroke-width="2.5" stroke-dasharray="22 200" transform="rotate(-90)"/>
        <circle r="18" fill="var(--navy)"/>
        <text y="6" text-anchor="middle" font-size="18" fill="#fff" font-family="Arimo,sans-serif">1</text>
      </g>
      <g transform="translate(60 333)">
        <circle r="25" fill="#fff" stroke="var(--ring)" stroke-width="4"/>
        <circle r="25" fill="none" stroke="var(--navy)" stroke-width="2.5" stroke-dasharray="18 200" transform="rotate(-90)"/>
        <circle r="25" fill="none" stroke="var(--red)" stroke-width="2.5" stroke-dasharray="0 18 22 200" transform="rotate(-90)"/>
        <circle r="18" fill="var(--red)"/>
        <text y="6" text-anchor="middle" font-size="18" fill="#fff" font-family="Arimo,sans-serif">2</text>
      </g>
      <g transform="translate(60 406)">
        <circle r="25" fill="#fff" stroke="var(--ring)" stroke-width="4"/>
        <circle r="25" fill="none" stroke="var(--navy)" stroke-width="2.5" stroke-dasharray="18 200" transform="rotate(-90)"/>
        <circle r="25" fill="none" stroke="var(--red)" stroke-width="2.5" stroke-dasharray="0 18 34 200" transform="rotate(-90)"/>
        <circle r="18" fill="var(--red)"/>
        <text y="6" text-anchor="middle" font-size="18" fill="#fff" font-family="Arimo,sans-serif">3</text>
      </g>
    </svg>
    <div class="timeline__label" style="top:55px;font-size:14px">START</div>
    <div class="timeline__label" style="top:445px;font-size:8px;font-style:italic">(Continue)</div>
  </div>

  <div class="t figure" style="left:148px;top:34px">FIGURE 5.</div>
  <div class="t" style="left:214px;top:26px;font-size:21px;line-height:24px;color:var(--sky)">Space Acquisition:</div>
  <div style="position:absolute;left:120px;top:70px;width:138px;height:1px;background:#fff"></div>
  <div class="t" style="left:263px;top:59px;font-size:20.5px;line-height:24px;font-weight:700">PURCHASE &amp; PROCESS DELIVERABLES</div>

  <div class="brand">
    <span class="brand__mark"></span>
    <span>Halvern Partners</span>
  </div>

  <div class="band" style="top:100px">
    <span style="left:0;width:374px">Roles &amp; Responsibilities</span>
    <span style="left:374px;width:141px">Process</span>
    <span style="left:515px;width:201px">Deliverables</span>
  </div>

  <!-- Row 1 -->
  <div class="t head" style="left:147px;top:137px">HVP TEAM</div>
  <ul class="t dots" style="left:147px;top:149px;line-height:12.2px">
    <li>Transaction Mgr</li><li>Portfolio Advisor</li><li>Broker</li><li>Project Mgr</li>
  </ul>
  <div class="t head" style="left:147px;top:222px">EXTERNAL TEAM</div>
  <ul class="t dots" style="left:147px;top:234px;line-height:12.2px">
    <li>Architect</li><li>Attorney</li><li>General Contractor</li><li>IT Consultant</li>
  </ul>
  <div class="t head" style="left:253px;top:137px">CLIENT TEAM</div>
  <ul class="t dots" style="left:253px;top:149px;line-height:12.2px">
    <li>Business Unit Mgr</li><li>Corporate RE Mgr</li><li>Risk Mgr</li><li>Regional Mgr</li><li>Local Operator</li><li>CEO/CFO</li><li>VP of Finance</li><li>Administrator</li><li>Lending Rep</li><li>Tax Advisor</li>
  </ul>
  <ul class="t dots sq" style="left:358px;top:136px">
    <li>Evaluate requirement in light<br>of client's strategic plan;<br>develop strategic plan, if<br>appropriate.</li>
    <li>Develop project management<br>strategy, budget, and<br>schedules.</li>
    <li>Review critical action date<br>report monthly.</li>
    <li>Establish KPIs.</li>
    <li>Distribute orientation binder.</li>
    <li>Review existing HVP/Client<br>customized Playbooks for<br>use and applicability.</li>
  </ul>
  <ul class="t dots sq proc" style="left:507px;top:139px">
    <li style="line-height:16px">Conduct Strategic<br>Planning Define</li>
    <li style="margin-top:6px">Client Requirements</li>
    <li style="margin-top:6px">Create Budget &amp; Schedule</li>
  </ul>
  <div class="t" style="left:651px;top:136px">
    <div><span class="num">1.1</span>&nbsp; Pre-Engagement Documents</div>
    <div class="sub">Authorization Letter</div>
    <div class="sub">Contact List</div>
    <div class="sub">Contracts</div>
    <div class="sub">RFQ Guidance</div>
    <div class="sub">Service Level Agreement (2)</div>
    <div class="sub">Commission Agreement</div>
    <div class="sub">Standard Reporting Templates</div>
    <div style="margin-top:3px"><span class="num">1.2</span>&nbsp; Client Needs Analysis (2)</div>
    <div style="padding-left:18px">Pre-Project Questionnaire</div>
    <div style="margin-top:2px"><span class="num">1.3</span>&nbsp; Strategic Plan <i>(no deliverable)</i></div>
    <div style="margin-top:3px"><span class="num">1.4</span>&nbsp; Schedule and Budget</div>
  </div>

  <div class="rule" style="top:303px"></div>

  <!-- Row 2 -->
  <div class="t" style="left:147px;top:326px;font-size:9.6px;line-height:12px">Portfolio Advisor, Transaction Manager and/or Broker</div>
  <div class="t center proc" style="left:494px;width:141px;top:322px">Develop Negotiation<br>Strategy</div>

  <div class="rule" style="top:358px"></div>

  <!-- Row 3 -->
  <div class="t" style="left:147px;top:375px">HVP Team, Client Team, External Team</div>
  <ul class="t dots sq" style="left:147px;top:385px">
    <li>Develop market research comps to determine fair value, market availability, and cost.</li>
    <li>Tour market with client and create shortlist of viable buildings.</li>
    <li>Develop tour list and report to client.</li>
  </ul>
  <div class="t center proc" style="left:494px;width:141px;top:387px">Conduct Market<br>Research and Analysis</div>
  <div class="t" style="left:651px;top:378px;line-height:14px">
    <div><span class="num">3.1</span>&nbsp; Market Survey Template</div>
    <div><span class="num">3.2</span>&nbsp; Financial Analysis</div>
    <div><span class="num">3.3</span>&nbsp; Own vs. Lease Analysis</div>
    <div><span class="num">3.4</span>&nbsp; Building Tour Spreadsheet</div>
    <div><span class="num">3.5</span>&nbsp; Building Tour Checklist</div>
  </div>
</section>

<!-- Sheet two -->
<section class="sheet sheet--bottom" aria-label="Space acquisition steps 4 to 8">
  <div class="col-process" style="top:68px"></div>

  <div class="timeline">
    <svg width="120" height="470" viewBox="0 0 120 470">
      <line x1="60" y1="120" x2="60" y2="400" stroke="var(--connector)" stroke-width="0.8"/>
      <path d="M57.5 142 L60 146 L62.5 142Z M57.5 205 L60 209 L62.5 205Z M57.5 289 L60 293 L62.5 289Z M57.5 374 L60 378 L62.5 374Z" fill="var(--connector)"/>
      <g transform="translate(60 109)">
        <circle r="25" fill="#fff" stroke="var(--ring)" stroke-width="4"/>
        <circle r="25" fill="none" stroke="var(--navy)" stroke-width="2.5" stroke-dasharray="18 200" transform="rotate(-90)"/>
        <circle r="25" fill="none" stroke="var(--red)" stroke-width="2.5" stroke-dasharray="0 18 42 200" transform="rotate(-90)"/>
        <circle r="18" fill="var(--light-blue)"/>
        <text y="6" text-anchor="middle" font-size="18" fill="#fff" font-family="Arimo,sans-serif">4</text>
      </g>
      <g transform="translate(60 173)">
        <circle r="25" fill="#fff" stroke="var(--ring)" stroke-width="4"/>
        <circle r="25" fill="none" stroke="var(--navy)" stroke-width="2.5" stroke-dasharray="18 200" transform="rotate(-90)"/>
        <circle r="25" fill="none" stroke="var(--red)" stroke-width="2.5" stroke-dasharray="0 18 42 200" transform="rotate(-90)"/>
        <circle r="25" fill="none" stroke="var(--light-blue)" stroke-width="2.5" stroke-dasharray="0 60 30 200" transform="rotate(-90)"/>
        <circle r="18" fill="var(--light-blue)"/>
        <text y="6" text-anchor="middle" font-size="18" fill="#fff" font-family="Arimo,sans-serif">5</text>
      </g>
      <g transform="translate(60 236)">
        <circle r="25" fill="#fff" stroke="var(--ring)" stroke-width="4"/>
        <circle r="25" fill="none" stroke="var(--navy)" stroke-width="2.5" stroke-dasharray="18 200" transform="rotate(-90)"/>
        <circle r="25" fill="none" stroke="var(--red)" stroke-width="2.5" stroke-dasharray="0 18 42 200" transform="rotate(-90)"/>
        <circle r="25" fill="none" stroke="var(--light-blue)" stroke-width="2.5" stroke-dasharray="0 60 55 200" transform="rotate(-90)"/>
        <circle r="18" fill="var(--light-blue)"/>
        <text y="6" text-anchor="middle" font-size="18" fill="#fff" font-family="Arimo,sans-serif">6</text>
      </g>
      <g transform="translate(60 320)">
        <circle r="25" fill="#fff" stroke="var(--ring)" stroke-width="4"/>
        <circle r="25" fill="none" stroke="var(--navy)" stroke-width="2.5" stroke-dasharray="18 200" transform="rotate(-90)"/>
        <circle r="25" fill="none" stroke="var(--red)" stroke-width="2.5" stroke-dasharray="0 18 42 200" transform="rotate(-90)"/>
        <circle r="25" fill="none" stroke="var(--light-blue)" stroke-width="2.5" stroke-dasharray="0 60 80 200" transform="rotate(-90)"/>
        <circle r="18" fill="var(--light-blue)"/>
        <text y="6" text-anchor="middle" font-size="18" fill="#fff" font-family="Arimo,sans-serif">7</text>
      </g>
      <g transform="translate(60 405)">
        <circle r="25" fill="#fff" stroke="var(--ring)" stroke-width="4"/>
        <circle r="25" fill="none" stroke="var(--navy)" stroke-width="2.5" stroke-dasharray="18 200" transform="rotate(-90)"/>
        <circle r="25" fill="none" stroke="var(--red)" stroke-width="2.5" stroke-dasharray="0 18 42 200" transform="rotate(-90)"/>
        <circle r="25" fill="none" stroke="var(--light-blue)" stroke-width="2.5" stroke-dasharray="0 60 72 200" transform="rotate(-90)"/>
        <circle r="25" fill="none" stroke="var(--orange)" stroke-width="2.5" stroke-dasharray="0 132 25 200" transform="rotate(-90)"/>
        <circle r="18" fill="var(--orange)"/>
        <text y="6" text-anchor="middle" font-size="18" fill="#fff" font-family="Arimo,sans-serif">8</text>
      </g>
    </svg>
    <div class="timeline__label" style="top:447px;font-size:14px">END</div>
  </div>

  <div class="t figure" style="left:148px;top:32px">FIGURE 5.</div>
  <div class="t" style="left:214px;top:25px;font-size:21px;line-height:24px;color:var(--muted)">Space Acquisition: <b style="color:#d9dee3">PURCHASE &amp; PROCESS DELIVERABLES</b></div>

  <div class="band" style="top:68px">
    <span style="left:0;width:374px">Roles &amp; Responsibilities</span>
    <span style="left:374px;width:141px">Process</span>
    <span style="left:515px;width:201px">Deliverables</span>
  </div>

  <!-- Row 4 -->
  <div class="t" style="left:147px;top:101px;font-size:9.4px;line-height:12.5px">
    Portfolio Advisor, Transaction Manager and/or Broker
    <ul class="dots sq"><li>Orchestrate competition.</li></ul>
  </div>
  <div class="t center proc" style="left:494px;width:141px;top:101px">
    <div style="color:var(--sky);font-size:10.5px">EXECUTION</div>
    <div>Negotiate with Short List</div>
  </div>
  <div class="rule" style="top:138px"></div>

  <!-- Row 5 -->
  <div class="t" style="left:147px;top:151px;font-size:9.4px;line-height:12px">Portfolio Advisor, Transaction Manager and/or Broker</div>
  <div class="t center proc" style="left:494px;width:141px;top:152px">Negotiate/Execute LOI and<br>Purchase &amp; Sale Agreement</div>
  <div class="t" style="left:651px;top:153px;line-height:14px">
    <div><span class="num">5.1</span> Letter of Intent</div>
    <div><span class="num">5.2</span> Purchase and Sale Agreement</div>
  </div>
  <div class="rule" style="top:192px"></div>

  <!-- Row 6 -->
  <div class="t" style="left:147px;top:207px;line-height:12.3px">
    <b>Portfolio Advisor, Transaction Manager and/or Broker, Tax Specialist, Lender Rep, Client<br>Legal, Client Risk, Third Party Vendors</b>
    <ul class="dots sq"><li>Due diligence may include environmental, structural, A&amp;E, title, clarity, appraisal, financial<br>appraisal, tax implications, etc.</li></ul>
  </div>
  <div class="t center proc" style="left:494px;width:141px;top:215px">Conduct Due Diligence</div>
  <div class="t" style="left:651px;top:209px;line-height:16px">
    <div><span class="num">6.1</span> Closing Checklist</div>
    <div><span class="num">6.2</span> Due Diligence Checklist</div>
  </div>
  <div class="rule" style="top:266px"></div>

  <!-- Row 7 -->
  <div class="t" style="left:147px;top:282px;line-height:12.3px">
    <b>Portfolio Advisor, Transaction Manager and/or Broker, Project Manager, Relocation<br>Manager, Lease Administrator</b>
    <ul class="dots sq">
      <li>Transaction manager brings in other service line experts (project management, lease<br>administration), if appropriate.</li>
      <li>If HVP is performing project mgmt, see PM Playbook.</li>
      <li>If HVP is <u>not</u> performing project mgmt, coordinate with client representative or landlord.</li>
    </ul>
  </div>
  <div class="t center proc" style="left:494px;width:141px;top:284px;line-height:14.5px">Develop Move/Project<br>Management Documentation<br>&amp; Transition to Project<br>Manager, if Applicable</div>
  <svg style="position:absolute;left:646px;top:278px" width="14" height="74" viewBox="0 0 14 74">
    <path d="M1 1 H6 V35 L11 37 L6 39 V73 H1" fill="none" stroke="var(--sky)" stroke-width="0.8"/>
  </svg>
  <div class="t link-note" style="left:681px;top:297px">See Project Management<br>and&nbsp; Facilities Management<br>Playbooks</div>
  <div class="rule" style="top:373px"></div>

  <!-- Row 8 -->
  <div class="t" style="left:146px;top:389px;line-height:12.2px">
    <b>Portfolio Advisor, Transaction Manager and/or Broker</b>
    <ul class="dots sq">
      <li>Benchmark performance and KPIs.</li>
      <li>Submit client satisfaction forms.</li>
      <li>Complete close-out summaries and corresponding critical date reports.</li>
      <li>Create client case study, if transaction size meets criteria.</li>
    </ul>
  </div>
  <div class="t center proc" style="left:494px;width:141px;top:387px">
    <div style="color:var(--sky);font-size:10.5px;line-height:14px">PERFORMANCE</div>
    <div style="line-height:12.5px">Measure/Demonstrate<br>Performance</div>
  </div>
  <div class="t" style="left:651px;top:390px;line-height:14px">
    <div><span class="num">8.1</span> KPI Documentation</div>
    <div><span class="num">8.2</span> Client Survey</div>
    <div><span class="num">8.3</span> Close-Out Package</div>
    <div><span class="num">8.4</span> Value-Added Matrix and Scorecard</div>
  </div>
</section>

</body>
</html>
```